Environmental "Pledge" Website

We are creating a template for a pledge campaign. Local residents visit a website and fill out a form. If they fill out the form and promise to do something good for the environment, they might win a prize.

They can watch a YouTube video that explains the contest. They can see a Google Map of everybody that has signed the pledge.

There is a blog on the homepage so the can see how the contest is going.

Industry/Entity Type

Campaign

```html
<!DOCTYPE html>
<html lang="en">
<head>
<meta charset="utf-8">
<title>Pledge Campaign – Home</title>
<link href="https://fonts.googleapis.com/css2?family=Oswald:wght@400;500&family=Lato:wght@400;700&family=Raleway:wght@300;700&display=swap" rel="stylesheet">
<style>
  :root {
    --green: #8cc63f;
    --black: #0a0a0a;
    --ink: #222222;
    --muted: #9a9a9a;
    --white: #ffffff;
    --panel: rgba(38, 34, 30, 0.88);
    --map: #ece8dd;
    --map-road: #f3d36b;
  }
  * { margin: 0; padding: 0; box-sizing: border-box; }
  html, body { width: 701px; height: 1200px; overflow: hidden; background: var(--white); }
  .page { position: relative; width: 701px; height: 1200px; overflow: hidden; font-family: "Lato", sans-serif; color: var(--ink); }

  .main-nav { position: absolute; left: 0; top: 0; width: 701px; height: 32px; background: var(--black); }
  .main-nav a { position: absolute; top: 0; height: 32px; line-height: 32px; font-family: "Raleway", sans-serif; font-weight: 700; font-size: 9px; color: var(--white); text-decoration: none; text-transform: uppercase; }
  .main-nav a.active { background: var(--green); width: 59px; text-align: center; }

  .hero { position: absolute; left: 0; top: 32px; width: 701px; height: 320px;
    background: linear-gradient(100deg, #eef5c6 0%, #d9e9a2 18%, #e9d3b6 40%, #d7a98a 60%, #b9785a 78%, #7a3e2a 100%); }
  .hero-card { position: absolute; left: 246px; top: 48px; width: 210px; height: 225px; background: var(--panel); text-align: center; color: var(--white); }
  .brand { position: absolute; left: 28px; top: 30px; width: 160px; height: 50px; }
  .brand-mark { position: absolute; left: 0; top: 2px; width: 46px; height: 46px; border-radius: 50%; background: var(--white); }
  .brand-name { position: absolute; left: 54px; top: 12px; width: 106px; text-align: center; font-family: "Raleway", sans-serif; font-weight: 300; font-size: 16px; line-height: 20px; letter-spacing: 0.3px; }
  .hero-title { position: absolute; left: 0; top: 108px; width: 100%; font-family: "Oswald", sans-serif; font-weight: 400; font-size: 18px; letter-spacing: -0.2px; }
  .hero-text { position: absolute; left: 15px; top: 142px; width: 180px; font-size: 9px; line-height: 14px; }
  .pledge-btn { position: absolute; left: 54px; top: 177px; width: 102px; height: 30px; line-height: 28px; border: 1px solid var(--green); outline: 1px solid var(--green); outline-offset: -4px; color: var(--green); font-family: "Raleway", sans-serif; font-weight: 700; font-size: 9.5px; }

  .section-title { position: absolute; font-family: "Oswald", sans-serif; font-weight: 400; font-size: 15px; color: var(--black); text-transform: uppercase; }
  .video { position: absolute; left: 43px; top: 408px; width: 299px; height: 197px; background: linear-gradient(160deg, #4a5048 0%, #3a3a33 40%, #2f2b25 70%, #4b4233 100%); }
  .video-play { position: absolute; left: 132px; top: 76px; width: 36px; height: 26px; }
  .video-bar { position: absolute; left: 0; bottom: 0; width: 100%; height: 20px; background: #111; }
  .video-progress { position: absolute; left: 0; top: 0; width: 60px; height: 2px; background: #d42020; }
  .video-time { position: absolute; left: 66px; top: 7px; font-size: 6px; color: #ddd; }

  .map { position: absolute; left: 358px; top: 408px; width: 300px; height: 197px; background: linear-gradient(135deg, #efebe1, #e6e2d4); overflow: hidden; }
  .map-thumb { position: absolute; left: 7px; top: 151px; width: 40px; height: 38px; border: 2px solid var(--white); background: linear-gradient(135deg, #8a8c7a, #6e705f); box-shadow: 0 1px 2px rgba(0,0,0,.3); }
  .map-thumb span { position: absolute; left: 3px; bottom: 2px; font-size: 5px; color: var(--white); }
  .map-zoom { position: absolute; left: 278px; top: 130px; width: 16px; height: 48px; }
  .map-tools { position: absolute; left: 218px; top: 181px; width: 76px; height: 14px; background: var(--white); box-shadow: 0 1px 2px rgba(0,0,0,.25); }

  .blog-card { position: absolute; width: 299px; height: 200px; }
  .blog-image { position: absolute; left: 0; top: 0; width: 299px; height: 151px; }
  .date-badge { position: absolute; left: 11px; top: 104px; width: 48px; height: 47px; background: var(--green); text-align: center; font-family: "Oswald", sans-serif; font-size: 8.5px; color: var(--black); }
  .date-badge svg { display: block; margin: 8px auto 4px; }
  .comment-badge { position: absolute; left: 11px; top: 151px; width: 48px; height: 48px; background: var(--black); text-align: center; font-family: "Oswald", sans-serif; font-size: 8.5px; color: var(--white); }
  .comment-badge svg { display: block; margin: 8px auto 4px; }
  .post-title { position: absolute; left: 75px; top: 164px; font-size: 10px; font-weight: 400; color: var(--ink); }
  .post-meta { position: absolute; left: 75px; top: 180px; font-size: 6px; color: var(--muted); }

  .site-footer { position: absolute; left: 0; top: 1123px; width: 701px; height: 77px; background: var(--black); color: var(--white); }
  .contact-heading { position: absolute; left: 42px; top: 20px; font-size: 9px; font-weight: 700; }
  .contact-line { position: absolute; left: 42px; font-size: 7px; color: #ddd; }
  .contact-line .accent { color: var(--green); }
  .social { position: absolute; left: 486px; top: 22px; display: flex; gap: 4px; }
  .social span { display: flex; align-items: center; justify-content: center; width: 21px; height: 21px; border: 1.5px solid #bbb; border-radius: 50%; }
  .copyright { position: absolute; left: 491px; top: 51px; font-size: 6.5px; font-weight: 400; color: #ddd; }
</style>
</head>
<body>
<div class="page">
  <nav class="main-nav">
    <a class="active" href="#" style="left:126px">Home</a>
    <a href="#" style="left:198px">About Us</a>
    <a href="#" style="left:273px">Fineprint</a>
    <a href="#" style="left:348px">Why Pledge</a>
    <a href="#" style="left:435px">Pledge Map</a>
    <a href="#" style="left:520px">Updates</a>
  </nav>

  <header class="hero" role="img" aria-label="Photo of a young woman drinking a glass of water">
    <div class="hero-card">
      <div class="brand">
        <span class="brand-mark"></span>
        <span class="brand-name">YOUR LOGO<br>HERE</span>
      </div>
      <h1 class="hero-title">LOREM IPSUM DOLOR</h1>
      <p class="hero-text">Lorem ipsum dolor sit amet, consectetuer aliquam erat volutpat. Ut wisi enim ...</p>
      <span class="pledge-btn">PLEDGE NOW</span>
    </div>
  </header>

  <h2 class="section-title" style="left:139px;top:376px">What's this about</h2>
  <h2 class="section-title" style="left:461px;top:376px">Who is pledging</h2>

  <div class="video" role="img" aria-label="Video explaining the contest, showing a family holding a fish by a lake">
    <svg class="video-play" viewBox="0 0 36 26"><rect width="36" height="26" rx="5" fill="rgba(0,0,0,.7)"/><path d="M14 7l10 6-10 6z" fill="#fff"/></svg>
    <div class="video-bar">
      <div class="video-progress"></div>
      <svg width="60" height="20" style="position:absolute;left:8px;top:0">
        <rect x="0" y="7" width="2" height="7" fill="#fff"/><rect x="4" y="7" width="2" height="7" fill="#fff"/>
        <path d="M16 7l4 3.5-4 3.5zM20 7l4 3.5-4 3.5z" fill="#fff"/><rect x="25" y="7" width="1.5" height="7" fill="#fff"/>
        <path d="M38 9h2l3-3v9l-3-3h-2z" fill="#fff"/>
      </svg>
      <span class="video-time">29:35 / 2:39:09</span>
      <svg width="55" height="20" style="position:absolute;right:4px;top:0">
        <circle cx="8" cy="10" r="3.5" fill="none" stroke="#fff" stroke-width="2"/>
        <rect x="22" y="6.5" width="9" height="7" fill="none" stroke="#fff" stroke-width="1.5"/>
        <path d="M41 7h3M41 7v3M52 7h-3M52 7v3M41 14h3M41 14v-3M52 14h-3M52 14v-3" stroke="#fff" stroke-width="1.5"/>
      </svg>
    </div>
  </div>

  <div class="map" role="img" aria-label="Map of everyone who has signed the pledge">
    <div class="map-thumb"><span>Earth</span></div>
    <svg class="map-zoom" viewBox="0 0 16 48">
      <rect x="0" y="0" width="16" height="14" fill="#fff"/><circle cx="8" cy="7" r="2.5" fill="none" stroke="#666" stroke-width="1.2"/>
      <rect x="0" y="18" width="16" height="30" fill="#fff"/>
      <path d="M5 25h6M8 22v6M5 41h6" stroke="#555" stroke-width="1.4"/><path d="M2 33h12" stroke="#ddd" stroke-width=".8"/>
    </svg>
    <div class="map-tools"></div>
  </div>

  <h2 class="section-title" style="left:42px;top:628px">Blog</h2>

  <article class="blog-card" style="left:43px;top:660px">
    <div class="blog-image" role="img" aria-label="Photo of a family paddling a red canoe" style="background:linear-gradient(180deg,#5b6a3a,#34452e 55%,#3b4b55)"></div>
    <div class="date-badge"><svg width="18" height="17" viewBox="0 0 18 17"><rect x="1" y="2" width="16" height="14" rx="1" fill="none" stroke="#000" stroke-width="1.6"/><rect x="1" y="2" width="16" height="4" fill="#000"/><path d="M4 9h2M8 9h2M12 9h2M4 12h2M8 12h2M12 12h2" stroke="#000" stroke-width="1.6"/></svg>20 DEC' 15</div>
    <div class="comment-badge"><svg width="18" height="16" viewBox="0 0 18 16"><path d="M9 1C4.5 1 1 3.8 1 7.2c0 1.8 1 3.4 2.6 4.5L2.8 15l3.8-2.3c.8.2 1.6.3 2.4.3 4.5 0 8-2.8 8-6.2S13.5 1 9 1z" fill="#fff"/></svg>565</div>
    <h3 class="post-title">Lorem ipsum dolor sit amet</h3>
    <p class="post-meta">By John smith &nbsp;|&nbsp; 17 Dec 2015 &nbsp;|&nbsp; 250 Comments</p>
  </article>

  <article class="blog-card" style="left:358px;top:660px">
    <div class="blog-image" role="img" aria-label="Photo of volunteers collecting litter on a beach" style="background:linear-gradient(180deg,#a9b8c4,#c9cdcb 45%,#cfc2a9)"></div>
    <div class="date-badge"><svg width="18" height="17" viewBox="0 0 18 17"><rect x="1" y="2" width="16" height="14" rx="1" fill="none" stroke="#000" stroke-width="1.6"/><rect x="1" y="2" width="16" height="4" fill="#000"/><path d="M4 9h2M8 9h2M12 9h2M4 12h2M8 12h2M12 12h2" stroke="#000" stroke-width="1.6"/></svg>20 DEC' 15</div>
    <div class="comment-badge"><svg width="18" height="16" viewBox="0 0 18 16"><path d="M9 1C4.5 1 1 3.8 1 7.2c0 1.8 1 3.4 2.6 4.5L2.8 15l3.8-2.3c.8.2 1.6.3 2.4.3 4.5 0 8-2.8 8-6.2S13.5 1 9 1z" fill="#fff"/></svg>565</div>
    <h3 class="post-title">Lorem ipsum dolor sit amet</h3>
    <p class="post-meta">By John smith &nbsp;|&nbsp; 17 Dec 2015 &nbsp;|&nbsp; 250 Comments</p>
  </article>

  <article class="blog-card" style="left:43px;top:886px">
    <div class="blog-image" role="img" aria-label="Photo of a child swimming in a lake" style="background:linear-gradient(180deg,#6f9a4a,#8a9a7a 30%,#8d8f85 60%,#6f6a5c)"></div>
    <div class="date-badge"><svg width="18" height="17" viewBox="0 0 18 17"><rect x="1" y="2" width="16" height="14" rx="1" fill="none" stroke="#000" stroke-width="1.6"/><rect x="1" y="2" width="16" height="4" fill="#000"/><path d="M4 9h2M8 9h2M12 9h2M4 12h2M8 12h2M12 12h2" stroke="#000" stroke-width="1.6"/></svg>20 DEC' 15</div>
    <div class="comment-badge"><svg width="18" height="16" viewBox="0 0 18 16"><path d="M9 1C4.5 1 1 3.8 1 7.2c0 1.8 1 3.4 2.6 4.5L2.8 15l3.8-2.3c.8.2 1.6.3 2.4.3 4.5 0 8-2.8 8-6.2S13.5 1 9 1z" fill="#fff"/></svg>565</div>
    <h3 class="post-title">Lorem ipsum dolor sit amet</h3>
    <p class="post-meta">By John smith &nbsp;|&nbsp; 17 Dec 2015 &nbsp;|&nbsp; 250 Comments</p>
  </article>

  <article class="blog-card" style="left:358px;top:886px">
    <div class="blog-image" role="img" aria-label="Photo of a city skyline reflected in a river at dusk" style="background:linear-gradient(180deg,#9a9bd0,#c7a6c2 35%,#2c3326 65%,#15181a)"></div>
    <div class="date-badge"><svg width="18" height="17" viewBox="0 0 18 17"><rect x="1" y="2" width="16" height="14" rx="1" fill="none" stroke="#000" stroke-width="1.6"/><rect x="1" y="2" width="16" height="4" fill="#000"/><path d="M4 9h2M8 9h2M12 9h2M4 12h2M8 12h2M12 12h2" stroke="#000" stroke-width="1.6"/></svg>20 DEC' 15</div>
    <div class="comment-badge"><svg width="18" height="16" viewBox="0 0 18 16"><path d="M9 1C4.5 1 1 3.8 1 7.2c0 1.8 1 3.4 2.6 4.5L2.8 15l3.8-2.3c.8.2 1.6.3 2.4.3 4.5 0 8-2.8 8-6.2S13.5 1 9 1z" fill="#fff"/></svg>565</div>
    <h3 class="post-title">Lorem ipsum dolor sit amet</h3>
    <p class="post-meta">By John smith &nbsp;|&nbsp; 17 Dec 2015 &nbsp;|&nbsp; 250 Comments</p>
  </article>

  <footer class="site-footer">
    <p class="contact-heading">Contact Info :</p>
    <p class="contact-line" style="top:38px">Your Company LTD. Street Name, 000000, City Name</p>
    <p class="contact-line" style="top:49px"><span class="accent">T: 1-000-000-0000</span> &nbsp;|&nbsp; E: <span class="accent">info@greenpledge.example</span></p>
    <div class="social" aria-label="Contact and share links">
      <span><svg width="11" height="8" viewBox="0 0 11 8"><rect x=".5" y=".5" width="10" height="7" fill="none" stroke="#ccc"/><path d="M.5 .5l5 4 5-4" fill="none" stroke="#ccc"/></svg></span>
      <span><svg width="10" height="10" viewBox="0 0 10 10"><circle cx="2" cy="5" r="1.5" fill="#ccc"/><circle cx="8" cy="2" r="1.5" fill="#ccc"/><circle cx="8" cy="8" r="1.5" fill="#ccc"/><path d="M2 5l6-3M2 5l6 3" stroke="#ccc"/></svg></span>
      <span><svg width="10" height="9" viewBox="0 0 10 9"><path d="M5 .5C2.5.5.5 2 .5 4c0 1 .6 1.9 1.5 2.5L1.5 8.5l2.2-1.2c.4.1.9.2 1.3.2 2.5 0 4.5-1.5 4.5-3.5S7.5.5 5 .5z" fill="#ccc"/></svg></span>
      <span><svg width="11" height="9" viewBox="0 0 11 9"><circle cx="4" cy="2.5" r="2" fill="#ccc"/><path d="M0 9c0-2.5 1.8-4 4-4s4 1.5 4 4z" fill="#ccc"/><circle cx="8.5" cy="3" r="1.5" fill="#ccc"/></svg></span>
      <span><svg width="10" height="8" viewBox="0 0 10 8"><rect x=".5" y=".5" width="9" height="7" rx="1" fill="none" stroke="#ccc"/><path d="M4 2.5l2.5 1.5L4 5.5z" fill="#ccc"/></svg></span>
      <span><svg width="8" height="10" viewBox="0 0 8 10"><path d="M4 .5a3.2 3.2 0 0 0-3.2 3.2C.8 6 4 9.5 4 9.5S7.2 6 7.2 3.7A3.2 3.2 0 0 0 4 .5z" fill="#ccc"/><circle cx="4" cy="3.7" r="1.1" fill="#0a0a0a"/></svg></span>
      <span><svg width="9" height="10" viewBox="0 0 9 10"><path d="M4.5 .8c-2 0-3 1.4-3 3.2v2.3L.5 7.8h8L7.5 6.3V4c0-1.8-1-3.2-3-3.2z" fill="#ccc"/><circle cx="4.5" cy="8.8" r="1" fill="#ccc"/></svg></span>
    </div>
    <p class="copyright">Copyright 2015 Company Name. All Rights Reserved</p>
  </footer>
</div>
</body>
</html>
```